Sleek business card design for digital agency.

Brief document attached for detailed description and inspiration. Looking for a minimalist sleek, cool, modern business card design.

Industry/Entity Type

Digital

```html
<!DOCTYPE html>
<html lang="en">
<head>
<meta charset="utf-8">
<title>Rivet Works – Business Card</title>
<link href="https://fonts.googleapis.com/css2?family=Open+Sans:wght@400;600;700&display=swap" rel="stylesheet">
<style>
  :root {
    --canvas: #e7e7e9;
    --card: #38383a;
    --ink: #0b0b0b;
    --white: #ffffff;
    --soft: #e2e2e2;
    --accent: #2ea3d5;
    --mark: #8c8c8e;
  }
  * { margin: 0; padding: 0; box-sizing: border-box; }
  html, body { width: 1200px; height: 1000px; overflow: hidden; }
  body {
    background: var(--canvas);
    font-family: "Open Sans", Arial, sans-serif;
    position: relative;
  }
  .card {
    position: absolute;
    background: var(--card);
    box-shadow: 3px 3px 4px rgba(0,0,0,0.35);
  }
  .card--front-tall { left: 60px; top: 300px; width: 249px; height: 408px; border-radius: 28px 0 18px 0; }
  .card--back-tall  { left: 323px; top: 300px; width: 249px; height: 408px; border-radius: 0 28px 0 18px; }
  .card--front-wide { left: 647px; top: 239px; width: 408px; height: 250px; border-radius: 0 28px 0 18px; }
  .card--back-wide  { left: 647px; top: 509px; width: 408px; height: 250px; border-radius: 28px 0 18px 0; }

  .wordmark {
    position: absolute;
    display: flex;
    align-items: center;
    gap: 8px;
    color: var(--ink);
    font-weight: 700;
    white-space: nowrap;
    letter-spacing: -0.5px;
  }
  .wordmark__dot { background: var(--ink); border-radius: 50%; flex: none; }
  .card--front-tall .wordmark { left: 20px; top: 180px; font-size: 29px; }
  .card--front-tall .wordmark__dot { width: 28px; height: 28px; }
  .card--front-wide .wordmark { left: 80px; top: 98px; font-size: 42px; gap: 12px; }
  .card--front-wide .wordmark__dot { width: 44px; height: 44px; }

  .brand-dot { position: absolute; background: var(--mark); border-radius: 50%; }
  .card--back-tall .brand-dot { left: 95px; top: 60px; width: 58px; height: 58px; }
  .card--back-wide .brand-dot { left: 72px; top: 28px; width: 66px; height: 66px; }

  .identity { position: absolute; white-space: nowrap; }
  .card--back-tall .identity { left: 43px; top: 143px; }
  .card--back-wide .identity { left: 149px; top: 38px; }
  .identity__name { color: var(--white); font-size: 18px; font-weight: 700; line-height: 24px; }
  .identity__name span { color: var(--accent); }
  .identity__role { color: var(--soft); font-size: 12.5px; font-weight: 700; line-height: 18px; }
  .identity__note { color: var(--soft); font-size: 11px; font-weight: 700; line-height: 18px; }

  .contacts { position: absolute; list-style: none; }
  .card--back-tall .contacts { left: 22px; top: 227px; }
  .card--back-wide .contacts { left: 130px; top: 114px; }
  .contacts li {
    display: flex; align-items: flex-start;
    color: var(--white); font-size: 11px; line-height: 16px;
    margin-bottom: 7px; white-space: nowrap;
  }
  .contacts svg { width: 12px; height: 12px; margin: 2px 8px 0 0; flex: none; }
  .contacts .sep { display: inline-block; width: 2px; height: 11px; background: var(--accent); margin: 0 4px; vertical-align: -1px; }
</style>
</head>
<body>

  <section class="card card--front-tall">
    <div class="wordmark"><span class="wordmark__dot"></span>Rivet Works</div>
  </section>

  <section class="card card--back-tall">
    <span class="brand-dot"></span>
    <div class="identity">
      <p class="identity__name">Daniel <span>Hartley</span></p>
      <p class="identity__role">Marketing Director</p>
      <p class="identity__note">Drink order: G&amp;T with cucumber</p>
    </div>
    <ul class="contacts">
      <li><svg viewBox="0 0 12 12"><path d="M1 6 6 1.5 11 6H9.5v4.5h-7V6Z" fill="none" stroke="#2ea3d5" stroke-width="1.5"/></svg><span>Level 2, 18 Marlow St<br>East Harbour NSW 2100</span></li>
      <li><svg viewBox="0 0 12 12"><rect x="3.5" y="1" width="5" height="10" rx="1.5" fill="#2ea3d5"/></svg><span>0400 555 012<i class="sep"></i>02 5550 1234</span></li>
      <li><svg viewBox="0 0 12 12"><rect x="1" y="2.5" width="10" height="7" fill="none" stroke="#2ea3d5" stroke-width="1.3"/><path d="M1 2.5 6 6.5 11 2.5" fill="none" stroke="#2ea3d5" stroke-width="1.3"/></svg><span>dhartley@rivetworks.com</span></li>
      <li><svg viewBox="0 0 12 12"><rect x="1.5" y="1.5" width="9" height="9" rx="1.5" fill="#2ea3d5"/></svg><span>social.rivetworks.com</span></li>
    </ul>
  </section>

  <section class="card card--front-wide">
    <div class="wordmark"><span class="wordmark__dot"></span>Rivet Works</div>
  </section>

  <section class="card card--back-wide">
    <span class="brand-dot"></span>
    <div class="identity">
      <p class="identity__name">Daniel <span>Hartley</span></p>
      <p class="identity__role">Marketing Director</p>
      <p class="identity__note">Drink order: G&amp;T with cucumber</p>
    </div>
    <ul class="contacts">
      <li><svg viewBox="0 0 12 12"><path d="M1 6 6 1.5 11 6H9.5v4.5h-7V6Z" fill="none" stroke="#2ea3d5" stroke-width="1.5"/></svg><span>Level 2, 18 Marlow St<br>East Harbour NSW 2100</span></li>
      <li><svg viewBox="0 0 12 12"><rect x="3.5" y="1" width="5" height="10" rx="1.5" fill="#2ea3d5"/></svg><span>0400 555 012<i class="sep"></i>02 5550 1234</span></li>
      <li><svg viewBox="0 0 12 12"><rect x="1" y="2.5" width="10" height="7" fill="none" stroke="#2ea3d5" stroke-width="1.3"/><path d="M1 2.5 6 6.5 11 2.5" fill="none" stroke="#2ea3d5" stroke-width="1.3"/></svg><span>dhartley@rivetworks.com</span></li>
      <li><svg viewBox="0 0 12 12"><rect x="1.5" y="1.5" width="9" height="9" rx="1.5" fill="#2ea3d5"/></svg><span>social.rivetworks.com</span></li>
    </ul>
  </section>

</body>
</html>
```